Brenton Wealth Management Flow Charts

I need help creating three flow charts for my businesses website. We want them to be simple but look professional. This is for a Wealth Management firm. I will attach a word document that has all of the descriptions for everything so you know what icons to use. We just want the chart to have an icon, the names of each step and the corresponding numbers. I will also include some examples of charts we liked as well. Once the winner is selected, we will need help with additional graphic design elements for our website ASAP.
- Goudy Roman

```html
<!DOCTYPE html>
<html lang="en">
<head>
<meta charset="utf-8">
<title>Client Process Flow Chart</title>
<link rel="stylesheet" href="https://fonts.googleapis.com/css2?family=Roboto:wght@700&display=swap">
<style>
  :root {
    --bg: #ffffff;
    --discovery: #98a6a3;
    --learning: #d3cd42;
    --planning: #bc8466;
    --execution: #6892bc;
    --alignment: #ffb64c;
    --review: #4fb6ac;
    --label: #ffffff;
    --icon: #1e3348;
  }
  html, body {
    margin: 0;
    padding: 0;
    width: 1200px;
    height: 722px;
    overflow: hidden;
    background: var(--bg);
  }
  .process-chart {
    display: block;
    width: 1200px;
    height: 722px;
  }
  .step { stroke: var(--bg); stroke-width: 4; stroke-linejoin: miter; }
  .step--discovery { fill: var(--discovery); }
  .step--learning { fill: var(--learning); }
  .step--planning { fill: var(--planning); }
  .step--execution { fill: var(--execution); }
  .step--alignment { fill: var(--alignment); }
  .step--review { fill: var(--review); }
  .step-label {
    font-family: "Roboto", Arial, sans-serif;
    font-weight: 700;
    font-size: 11px;
    fill: var(--label);
    letter-spacing: 0.1px;
  }
  .icon {
    fill: none;
    stroke: var(--icon);
    stroke-width: 1.8;
    stroke-linecap: round;
    stroke-linejoin: round;
  }
</style>
</head>
<body>
<svg class="process-chart" viewBox="0 0 1280 770" role="img" aria-label="Client process: Discovery Meeting, Learning, then a cycle of Planning, Execution, Alignment and Review">

  <!-- Linear lead-in steps -->
  <path class="step step--discovery" d="M263,295 L451,295 L451,267 L478,340 L451,406 L451,386 L263,386 Z"/>
  <path class="step step--learning" d="M468,295 L626,295 L626,267 L655,340 L626,406 L626,386 L468,386 L480,340 Z"/>

  <!-- Cycle steps -->
  <path class="step step--planning" d="M645,295 L735,295 A167,167 0 0 1 860,238 L860,213 L890,285 L860,352 L860,330 A75,75 0 0 0 785,386 L642,386 L655,340 Z"/>
  <path class="step step--execution" d="M878,240 A167,167 0 0 1 1025,407 L1050,407 L980,438 L910,407 L933,407 A75,75 0 0 0 876,333 L893,285 Z"/>
  <path class="step step--alignment" d="M1023,425 A167,167 0 0 1 858,573 L856,598 L826,530 L856,458 L856,481 A75,75 0 0 0 933,425 L975,440 Z"/>
  <path class="step step--review" d="M838,571 A167,167 0 0 1 691,405 L666,405 L737,374 L806,405 L783,405 A75,75 0 0 0 840,478 L825,528 Z"/>

  <!-- Discovery meeting: two conversation markers -->
  <g class="icon">
    <circle cx="298" cy="340" r="8.5"/>
    <circle cx="327" cy="340" r="8.5"/>
  </g>
  <text class="step-label" x="358" y="337">DISCOVERY</text>
  <text class="step-label" x="358" y="351">MEETING</text>

  <!-- Learning: structure + target -->
  <g class="icon">
    <rect x="511" y="329" width="7" height="6"/>
    <rect x="505" y="344" width="7" height="6"/>
    <rect x="518" y="344" width="7" height="6"/>
    <path d="M514.5,335 V339.5 H508.5 V344 M514.5,339.5 H521.5 V344"/>
    <circle cx="544" cy="340" r="6.5"/>
    <circle cx="544" cy="340" r="2"/>
    <path d="M544,330 V333.5 M544,346.5 V350 M534,340 H537.5 M550.5,340 H554"/>
  </g>
  <text class="step-label" x="565" y="344">LEARNING</text>

  <!-- Planning: pie chart -->
  <g class="icon">
    <path d="M773,301 A8,8 0 1 0 781,309 H773 Z"/>
    <path d="M776,298 A8,8 0 0 1 784,306 H776 Z"/>
  </g>
  <text class="step-label" x="760" y="337" text-anchor="middle">PLANNING</text>

  <!-- Execution: bar chart -->
  <g class="icon">
    <path d="M931,297 V315 H950"/>
    <path d="M935,313 V305 M939,313 V300 M943,313 V303 M947,313 V298"/>
  </g>
  <text class="step-label" x="955" y="337" text-anchor="middle">EXECUTION</text>

  <!-- Alignment: briefcase -->
  <g class="icon">
    <rect x="931" y="474" width="18" height="13" rx="1.5"/>
    <path d="M936,474 V471 H944 V474 M931,480 H949"/>
  </g>
  <text class="step-label" x="931" y="507" text-anchor="middle">ALIGNMENT</text>

  <!-- Review: document with magnifier -->
  <g class="icon">
    <path d="M777,487 H766 V470 H774 L779,475 V479"/>
    <path d="M769,476 H774 M769,480 H773 M769,484 H772"/>
    <circle cx="779" cy="484" r="3"/>
    <path d="M781.2,486.2 L784,489"/>
  </g>
  <text class="step-label" x="773" y="507" text-anchor="middle">REVIEW</text>
</svg>
</body>
</html>
```